Brisk Hounds Dog Behaviour, Training and Natural Healthcare Business Card Design

I am an experienced and qualified dog behavioural trainer and natural animal healthcare consultant offering a range of services to help pet dog owners with the "whole dog".
COLOURS: A soft light blue in the background - can be fading out or split, red should also feature
LOGO: Dog, healing hands, silhouette, shadow
SERVICES: Behaviour Consults, Training, Complex Skills Coaching Walking Coaching, Diet & Nutrition, Environmental Enrichment, Lifestyle and Lifestage Adaptations, Massage, Natural Health Options
BY LINE: Happy Dogs, Happy Owners
VALUES: Promoting communication and connection between dogs and their owners.
FOCUS: Nutritional guidance and environmental adaptation are often needed to complete the package and increase the success rate of training and behaviour modification.

Target Market(s)

Everyone who has a dog who they wish to improve their relationship with

Industry/Entity Type

Communication

Contact Information for Business Card

Brisk Hounds, Renata Walcott, 0472 680351, briskhounds7@mailnest.example, www.briskhounds7.example, Qualified Dog Behavioural Trainer and Natural Animal Healthcare Consultant

Font styles to use
Sans Serif
Script

Colors
85cae6
ec2027

Requirements
Must have
• A clear indication that it is a dog services business. A raised feature
Should not have
• Pawprints, cartoons

```html
<!DOCTYPE html>
<html lang="en">
<head>
<meta charset="utf-8">
<title>Brisk Hounds Business Card</title>
<link rel="stylesheet" href="https://fonts.googleapis.com/css2?family=Arimo:wght@400;700&family=Tinos&family=Bodoni+Moda:wght@500&display=swap">
<style>
  :root {
    --stage: #e9ecee;
    --card: #ffffff;
    --teal: #1fb0b8;
    --ink: #111111;
    --coat-dark: #2a2118;
    --coat-tan: #b98a52;
    --coat-light: #d4a56c;
  }
  * { box-sizing: border-box; margin: 0; padding: 0; }
  html, body { width: 1200px; height: 900px; overflow: hidden; background: var(--stage); }
  .card {
    position: absolute; left: 100px; top: 160px;
    width: 1000px; height: 580px;
    background: var(--card);
    overflow: hidden;
    box-shadow: 0 8px 24px rgba(0,0,0,.18);
  }
  .card__band { position: absolute; left: 0; top: 0; width: 1000px; height: 580px; }
  .card__owner {
    position: absolute; left: 160px; top: 20px;
    font-family: "Tinos", serif; font-size: 28px; color: var(--ink);
    transform: scaleX(.85); transform-origin: left;
    white-space: nowrap;
  }
  .photo { position: absolute; }
  .photo--seated-dog {
    left: 40px; top: 70px; width: 290px; height: 300px;
    border-radius: 48% 48% 0 0 / 30% 30% 0 0;
    background: radial-gradient(ellipse at 55% 30%, var(--coat-tan) 0%, var(--coat-dark) 55%, var(--coat-light) 100%);
  }
  .photo--profile-dog {
    left: 720px; top: 270px; width: 280px; height: 310px;
    border-radius: 60% 0 0 0 / 45% 0 0 0;
    background: radial-gradient(ellipse at 60% 50%, var(--coat-light) 0%, var(--coat-tan) 60%, var(--coat-dark) 100%);
  }
  .brand {
    position: absolute; left: 400px; top: 60px; width: 480px; text-align: center;
    font-family: "Arimo", sans-serif; color: var(--ink);
  }
  .brand__name { font-weight: 700; font-size: 56px; line-height: 1; }
  .brand__rule { height: 3px; background: var(--teal); margin: 12px 20px 10px; }
  .brand__role { font-size: 17px; line-height: 1.35; }
  .contact {
    position: absolute; left: 390px; top: 300px; width: 320px;
    font-family: "Arimo", sans-serif; font-size: 20px; line-height: 1.4; color: var(--ink);
    white-space: nowrap;
  }
  .phone {
    position: absolute; left: 350px; top: 425px;
    font-family: "Bodoni Moda", serif; font-weight: 500; font-size: 120px; line-height: 1;
    color: var(--ink); transform: scaleX(.5); transform-origin: left;
    white-space: nowrap;
  }
</style>
</head>
<body>
  <div class="card">
    <svg class="card__band" viewBox="0 0 1000 580" aria-hidden="true">
      <polygon points="0,340 290,340 340,400 1000,400 1000,580 0,580" fill="var(--teal)"/>
    </svg>
    <div class="photo photo--seated-dog" role="img" aria-label="Photo of a seated German Shepherd dog"></div>
    <div class="photo photo--profile-dog" role="img" aria-label="Photo of a tan dog's head in profile"></div>
    <div class="card__owner">Renata Walcott</div>
    <div class="brand">
      <div class="brand__name">Brisk Hounds</div>
      <div class="brand__rule"></div>
      <div class="brand__role">Qualified Dog Behavioural<br>Trainer and Natural Animal Healthcare Consultant</div>
    </div>
    <div class="contact">
      <div class="contact__web">www.briskhounds7.example</div>
      <div class="contact__email">briskhounds7@mailnest.example</div>
    </div>
    <div class="phone">0472 680351</div>
  </div>
</body>
</html>
```